South Maple Ridge (by the numbers)

We (city communications office of South Maple Ridge, Arkansas) are launching a magazine to be delivered to every house in the community. We would like the first inside page to be an infographic of the important and interesting "numbers" from 2017. We want it to be visually interesting and convey the huge amount of important services we provide our residents. I have included a document with the relevant statistics to be used.

Target Market(s)

Residents of our city

Industry/Entity Type

House

Colors

Designer to choose colors to be used in the design.

Requirements
Must have
• Our logo must be prominent. The dimensions should be able to fit onto a standard full page magazine. If the infographic is best displayed on two pages we will accept that as well, and change our layout.
Nice to have
• Not every statistic we have provided must be used but if they can be, that is preferable. I have also included some inspirational infographics that appealed to me and inspired the idea, but I am excited about new concepts that might not look anything like those that I have provided.
Should not have
• The design should not have anything incorporated that cannot be presented to families in our community. It must be all ages friendly.

```html
<!DOCTYPE html>
<html lang="en">
<head>
<meta charset="utf-8">
<title>South Maple Ridge by the Numbers 2017</title>
<link rel="stylesheet" href="https://fonts.googleapis.com/css2?family=Oswald:wght@300;400&family=Montserrat:wght@600;700;800&display=swap">
<style>
  :root {
    --bg: #f5f7ef;
    --hill: #e8eedb;
    --ink: #2b2b2b;
    --title-box: #2e2e2e;
    --lime: #8cc63f;
    --stat: #4d4d4d;
    --label: #333333;
    --accent-blue: #1d5fa6;
    --rule: #3a3a3a;
    --road: #545454;
  }
  html, body { margin: 0; padding: 0; overflow: hidden; }
  body { width: 934px; height: 1200px; background: var(--bg); position: relative; font-family: "Montserrat", Arial, sans-serif; }
  .hills { position: absolute; inset: 0; pointer-events: none; }
  .title-block { position: absolute; left: 41px; top: 0; width: 348px; height: 309px; background: var(--title-box); }
  .title-block h1 { margin: 0; position: absolute; left: 30px; top: 50px; font-family: "Oswald", "Arial Narrow", sans-serif; font-weight: 300; color: var(--lime); font-size: 70px; line-height: 62px; letter-spacing: 1px; }
  .title-block .subtitle { position: absolute; left: 32px; top: 248px; font-family: "Montserrat", Arial, sans-serif; font-weight: 600; color: #fff; font-size: 22px; }
  .year-tab { position: absolute; left: 298px; top: 92px; width: 80px; height: 165px; background: var(--lime); }
  .year-tab span { position: absolute; left: 50%; top: 50%; transform: translate(-50%, -50%) rotate(-90deg); font-family: "Oswald", "Arial Narrow", sans-serif; font-weight: 400; font-size: 52px; color: var(--ink); letter-spacing: 2px; }
  .grid-lines { position: absolute; inset: 0; }
  .stat { position: absolute; width: 218px; text-align: center; }
  .stat .icon { display: block; margin: 0 auto; border-radius: 18px; }
  .stat .label { font-weight: 700; font-size: 13px; line-height: 16px; color: var(--label); margin-top: 12px; }
  .stat .label .hl { color: var(--accent-blue); }
  .stat .value { font-weight: 800; font-size: 32px; line-height: 36px; color: var(--stat); letter-spacing: 1px; }
  .park-scene { position: absolute; left: 0; top: 930px; width: 934px; height: 215px; background: linear-gradient(180deg, rgba(166,206,57,0) 0%, #b5d55f 45%, #7fb23a 100%); }
  .road { position: absolute; left: 0; top: 1145px; width: 934px; height: 55px; background: var(--road); }
  .road::before { content: ""; position: absolute; left: 0; top: 0; width: 100%; height: 10px; background: #6d6d6d; }
</style>
</head>
<body>
  <svg class="hills" width="934" height="1200" aria-hidden="true">
    <circle cx="520" cy="60" r="140" fill="var(--hill)"/>
    <circle cx="760" cy="40" r="170" fill="var(--hill)"/>
    <circle cx="400" cy="180" r="90" fill="var(--hill)"/>
  </svg>

  <header class="title-block">
    <h1>SOUTH<br>MAPLE<br>RIDGE</h1>
    <div class="subtitle">by the Numbers</div>
    <div class="year-tab"><span>2017</span></div>
  </header>

  <svg class="grid-lines" width="934" height="1200" aria-hidden="true">
    <g stroke="var(--rule)" stroke-width="1.5">
      <line x1="458" y1="190" x2="458" y2="860"/>
      <line x1="675" y1="190" x2="675" y2="860"/>
      <line x1="240" y1="420" x2="240" y2="860"/>
      <line x1="24" y1="407" x2="910" y2="407"/>
      <line x1="24" y1="641" x2="910" y2="641"/>
    </g>
    <g fill="var(--rule)">
      <circle cx="240" cy="407" r="5"/><circle cx="458" cy="407" r="5"/><circle cx="675" cy="407" r="5"/>
      <circle cx="240" cy="641" r="5"/><circle cx="458" cy="641" r="5"/><circle cx="675" cy="641" r="5"/>
    </g>
  </svg>

  <div class="stat" style="left:458px;top:198px;">
    <div class="icon" role="img" aria-label="Group of residents icon" style="width:120px;height:110px;background:#f2b27a;"></div>
    <div class="label">Population</div>
    <div class="value">65,004</div>
  </div>
  <div class="stat" style="left:675px;top:198px;">
    <div class="icon" role="img" aria-label="Family of park visitors icon" style="width:120px;height:110px;background:#9a8b80;"></div>
    <div class="label">Visitors to <span class="hl">Alder Park</span></div>
    <div class="value">779,621</div>
  </div>

  <div class="stat" style="left:22px;top:430px;">
    <div class="icon" role="img" aria-label="Police officer with phone icon" style="width:130px;height:110px;background:#2f4f86;"></div>
    <div class="label"><span class="hl">Police 911</span> calls</div>
    <div class="value">26,660</div>
  </div>
  <div class="stat" style="left:240px;top:430px;">
    <div class="icon" role="img" aria-label="Firefighter with phone icon" style="width:130px;height:110px;background:#d9412f;"></div>
    <div class="label"><span class="hl">Fire 911</span> calls</div>
    <div class="value">12,560</div>
  </div>
  <div class="stat" style="left:458px;top:430px;">
    <div class="icon" role="img" aria-label="Road winding through trees icon" style="width:120px;height:100px;background:#5fa84a;"></div>
    <div class="label">Tons of asphalt used in<br>repairing potholes and<br>street overlays</div>
    <div class="value">5,952</div>
  </div>
  <div class="stat" style="left:675px;top:430px;">
    <div class="icon" role="img" aria-label="Garbage bag and recycling bin icon" style="width:120px;height:100px;background:#e6a92a;"></div>
    <div class="label">Tons of Household<br>garbage collected</div>
    <div class="value">16,768</div>
  </div>

  <div class="stat" style="left:22px;top:662px;">
    <div class="icon" role="img" aria-label="Tire with recycling symbol icon" style="width:100px;height:110px;background:#3a3a3a;border-radius:50px;"></div>
    <div class="label">Used tires recycled</div>
    <div class="value">4,221</div>
  </div>
  <div class="stat" style="left:240px;top:662px;">
    <div class="icon" role="img" aria-label="Green leaves icon" style="width:100px;height:100px;background:#8cc63f;border-radius:50px;"></div>
    <div class="label">Cubic yards of green<br>(yard) waste collected</div>
    <div class="value">116,675</div>
  </div>
  <div class="stat" style="left:458px;top:662px;">
    <div class="icon" role="img" aria-label="Park with trees and bench icon" style="width:130px;height:100px;background:#9ccf5a;"></div>
    <div class="label">neighborhood<br>parks</div>
    <div class="value">34</div>
  </div>
  <div class="stat" style="left:675px;top:662px;">
    <div class="icon" role="img" aria-label="Playground with slide and seesaw icon" style="width:140px;height:100px;background:#e0703a;"></div>
    <div class="label">Open Arms Inclusive<br>Playgrounds built for kids<br>with special needs</div>
    <div class="value">1</div>
  </div>

  <div class="park-scene" role="img" aria-label="Park scene with green trees, street lamps and fire hydrants along the road"></div>
  <div class="road"></div>
</body>
</html>
```